Label for Custom Gin Botle

Design an label for Gin botle, need label asap sorry

Target Market(s)

Our customers

Requirements
Must have
• Classic/expensive look

```html
<!DOCTYPE html>
<html lang="nl">
<head>
<meta charset="utf-8">
<title>Stellage Gin – Label</title>
<link rel="stylesheet" href="https://fonts.googleapis.com/css2?family=Arvo:wght@700&family=Roboto:wght@400;500;700&family=Staatliches&display=swap">
<style>
  :root {
    --backdrop: #ababab;
    --label-green: #2f7a3e;
    --damask-tone: #7d9a78;
    --diamond-green: #2b6f39;
    --diamond-edge: #3c8a4a;
    --ink-white: #ffffff;
  }
  html, body {
    margin: 0;
    padding: 0;
    width: 1039px;
    height: 1200px;
    overflow: hidden;
    background: var(--backdrop);
  }
  .canvas {
    position: relative;
    width: 1039px;
    height: 1200px;
    display: flex;
    align-items: center;
    justify-content: center;
  }
  .gin-label {
    width: 960px;
    height: 395px;
    display: block;
  }
  .brand-name { font-family: "Roboto", sans-serif; font-weight: 700; fill: var(--ink-white); }
  .arched-title { font-family: "Arvo", serif; font-weight: 700; fill: var(--ink-white); }
  .gin-word { font-family: "Staatliches", sans-serif; fill: var(--ink-white); }
  .small-print { font-family: "Roboto", sans-serif; font-weight: 400; fill: var(--ink-white); }
  .spec-print { font-family: "Roboto", sans-serif; font-weight: 500; fill: var(--ink-white); }
</style>
</head>
<body>
<main class="canvas">
  <svg class="gin-label" viewBox="0 0 960 395" xmlns="http://www.w3.org/2000/svg">
    <defs>
      <linearGradient id="damaskWash" x1="0" y1="0" x2="1" y2="1">
        <stop offset="0" stop-color="#3d7f45"/>
        <stop offset="0.5" stop-color="#54895a"/>
        <stop offset="1" stop-color="#3b7e44"/>
      </linearGradient>
      <path id="titleArc" d="M 350 245 A 150 150 0 0 1 610 245"/>
      <path id="siteArc" d="M 70 140 A 48 48 0 0 1 166 140"/>
      <path id="batchArc" d="M 824 131 A 24 24 0 0 1 872 131"/>
      <path id="bottleArc" d="M 824 205 A 24 24 0 0 1 872 205"/>
    </defs>

    <!-- label body -->
    <rect class="label-base" width="960" height="395" fill="var(--label-green)"/>
    <g role="img" aria-label="Groen damastpatroon over het hele etiket">
      <rect width="960" height="395" fill="url(#damaskWash)"/>
    </g>
    <rect class="inner-frame" x="29" y="66" width="902" height="262" fill="none" stroke="var(--damask-tone)" stroke-opacity="0.35" stroke-width="2"/>

    <!-- centre diamond -->
    <g class="title-diamond">
      <polygon points="480,40 637,194 480,350 323,194" fill="var(--diamond-green)" stroke="var(--diamond-edge)" stroke-width="2"/>
      <text class="brand-name" x="480" y="114" text-anchor="middle" font-size="17" letter-spacing="0.5">VELDHOF</text>
      <text class="arched-title" font-size="40" letter-spacing="1">
        <textPath href="#titleArc" startOffset="50%" text-anchor="middle">STELLAGE</textPath>
      </text>
      <text class="gin-word" x="480" y="254" text-anchor="middle" font-size="62" letter-spacing="2">GIN</text>
      <text class="spec-print" x="480" y="296" text-anchor="middle" font-size="10">500ML</text>
      <text class="spec-print" x="480" y="312" text-anchor="middle" font-size="10">40% VOL</text>
    </g>

    <!-- left column -->
    <g class="left-panel">
      <text class="small-print" font-size="14" letter-spacing="0.5">
        <textPath href="#siteArc" startOffset="50%" text-anchor="middle">VELDHOF.EU</textPath>
      </text>
      <text class="gin-word" x="118" y="147" text-anchor="middle" font-size="20">GIN</text>
      <rect class="notice-square" x="106" y="182" width="24" height="24" fill="none" stroke="var(--ink-white)" stroke-width="2"/>
      <rect class="notice-square" x="106" y="219" width="24" height="24" fill="none" stroke="var(--ink-white)" stroke-width="2"/>
      <text class="small-print" x="118" y="279" text-anchor="middle" font-size="13">Kan Sporen Van</text>
      <text class="small-print" x="118" y="298" text-anchor="middle" font-size="13">Allergenen Bevatten</text>
    </g>

    <!-- right column -->
    <g class="right-panel">
      <text class="small-print" font-size="11" letter-spacing="0.5">
        <textPath href="#batchArc" startOffset="50%" text-anchor="middle">BATCH</textPath>
      </text>
      <circle class="fill-in-dot" cx="848" cy="131" r="17" fill="var(--ink-white)"/>
      <text class="small-print" font-size="11" letter-spacing="0.5">
        <textPath href="#bottleArc" startOffset="50%" text-anchor="middle">BOTTLE</textPath>
      </text>
      <circle class="fill-in-dot" cx="848" cy="205" r="17" fill="var(--ink-white)"/>
      <text class="small-print" x="848" y="256" text-anchor="middle" font-size="13">Lindenhof 7</text>
      <text class="small-print" x="848" y="275" text-anchor="middle" font-size="13">6512 Ab Arnhem</text>
      <text class="small-print" x="848" y="300" text-anchor="middle" font-size="13">INFO@STELLAGE-GIN.COM</text>
    </g>
  </svg>
</main>
</body>
</html>
```